Las Vegas FUN Save the Date cards for wedding

Looking for save the date's for our wedding that will be in Las Vegas. I have attached what I would like them to look like and wondering if it is simple/easy to do this design as a postcard sized piece.

Look/Feel -- Playing Card very similar to design shown.
Information:

Save the date
Derek Holloway & Jamie Fortescue are getting married
Date: 1/23/2016
In fabulous Las Vegas
Invitations, details and a website to follow soon
*Yes, Marigold and Hazel will be there too*

Need this quick. Please take liberty with design, font and layout of the text on the back. Please try to keep the front of the postcard similar (but some difference) to whats in the attached pic.

Link: http://quirkyvows.example/2013/05/printcraze-tips-and-tricks

Thanks.
Jamie
415-555-0187

Target Market(s)

150-250 of our closest friends

Industry/Entity Type

Wedding

Font styles to use
Decorative
Script
Other font styles liked:
• Gotham

Requirements
Must have
• Look a lot like the attachment but take some FUN creative liberties -- esp on front that looks like the playing card...perhaps liberties in the squiggly line part.
Nice to have
• Different color options

```html
<!DOCTYPE html>
<html lang="en">
<head>
<meta charset="utf-8">
<title>Save the Date – Derek Holloway &amp; Jamie Fortescue</title>
<link rel="stylesheet" href="https://fonts.googleapis.com/css2?family=Montserrat:wght@400;600;700;800&family=Rock+Salt&display=swap">
<style>
  :root {
    --backdrop: #000000;
    --paper: #f1efef;
    --blush: #d9aaa6;
    --blush-soft: #ead0cd;
    --slate: #5d5d60;
    --chalk: #3a3a3a;
    --chalk-deep: #2c2c2c;
    --white: #ffffff;
    --ink: #222222;
    --muted: #9a9a9a;
  }
  * { box-sizing: border-box; margin: 0; padding: 0; }
  html, body {
    width: 807px; height: 1200px; overflow: hidden;
    background: var(--backdrop);
    font-family: "Montserrat", Arial, sans-serif;
  }
  .canvas { position: relative; width: 807px; height: 1200px; }

  /* ---------- Front of postcard ---------- */
  .card-front {
    position: absolute; left: 22px; top: 27px; width: 764px; height: 560px;
    background: var(--paper);
  }
  .flourish-frame {
    position: absolute; inset: 14px;
    border: 54px solid var(--blush-soft);
    outline: 3px solid var(--blush);
    outline-offset: -30px;
  }
  .crest {
    position: absolute; left: 222px; top: 90px; width: 320px; height: 262px;
    background: radial-gradient(ellipse at center, #e2e2e4 0%, #b9b9bd 70%, #a3a3a8 100%);
    border-radius: 40% 40% 30% 30% / 35% 35% 25% 25%;
  }
  .crest-plate {
    position: absolute; left: 257px; top: 228px; width: 250px; height: 108px;
    background: var(--white);
    border: 3px solid var(--slate);
    border-radius: 18px;
  }
  .couple-front {
    position: absolute; left: 257px; top: 228px; width: 250px; height: 108px;
    display: flex; flex-direction: column; align-items: center; justify-content: center;
    text-align: center; color: var(--ink); white-space: nowrap;
    font-weight: 800; font-size: 15px; line-height: 22px; text-transform: uppercase;
  }
  .front-rule {
    position: absolute; left: 150px; top: 451px; width: 464px; height: 2px;
    background: var(--slate);
  }
  .front-ribbon { position: absolute; left: 217px; top: 420px; }
  .front-ribbon-text {
    position: absolute; left: 217px; top: 420px; width: 330px; height: 62px;
    display: flex; align-items: center; justify-content: center;
    color: var(--white); font-weight: 700; font-size: 24px; letter-spacing: 1px;
  }

  /* ---------- Back of postcard ---------- */
  .card-back {
    position: absolute; left: 22px; top: 613px; width: 764px; height: 565px;
    background: radial-gradient(ellipse at 40% 45%, var(--chalk) 0%, var(--chalk-deep) 100%);
    color: var(--white);
  }
  .ornament { position: absolute; background: linear-gradient(90deg, transparent, rgba(255,255,255,.55), transparent); height: 16px; border-radius: 8px; }
  .ornament-top { left: 90px; top: 38px; width: 240px; }
  .ornament-bottom { left: 30px; top: 512px; width: 360px; }

  .message { position: absolute; left: 20px; top: 0; width: 376px; text-align: center; }
  .save-title {
    position: absolute; left: 0; top: 76px; width: 100%;
    font-weight: 700; font-size: 30px; letter-spacing: 1px;
  }
  .back-ribbon { position: absolute; left: 18px; }
  .back-ribbon-text {
    position: absolute; left: 0; width: 100%; height: 46px;
    display: flex; align-items: center; justify-content: center;
    color: var(--ink); font-weight: 700;
  }
  .date-text { top: 130px; font-size: 24px; }
  .married-text { top: 352px; font-size: 19px; letter-spacing: .5px; }
  .couple-back {
    position: absolute; left: 0; top: 206px; width: 100%;
    font-family: "Rock Salt", cursive; font-size: 23px; line-height: 38px;
    text-transform: uppercase; color: #e9e9e9; white-space: nowrap;
  }
  .couple-back .joiner { font-size: 18px; display: block; }
  .in-fabulous {
    position: absolute; left: 0; top: 422px; width: 100%;
    font-weight: 700; font-size: 13px; letter-spacing: 1px; text-transform: uppercase;
  }
  .city {
    position: absolute; left: 0; top: 446px; width: 100%;
    font-weight: 800; font-size: 42px; letter-spacing: 1px; text-transform: uppercase;
  }

  .stamp-box {
    position: absolute; left: 632px; top: 33px; width: 108px; height: 108px;
    background: var(--white);
  }
  .address-line {
    position: absolute; left: 462px; width: 283px; height: 1px;
    background: #6a6a6a;
  }
  .follow-note {
    position: absolute; left: 470px; top: 480px; width: 280px; text-align: center;
    font-size: 12px; line-height: 18px; letter-spacing: 1px; color: var(--muted);
    text-transform: uppercase;
  }
</style>
</head>
<body>
<div class="canvas">

  <section class="card-front">
    <div class="flourish-frame" role="img" aria-label="Blush pink playing-card style flourish border"></div>
    <div class="crest" role="img" aria-label="Grey baroque crest ornament framing the couple's names"></div>
    <div class="crest-plate"></div>
    <p class="couple-front"><span>Derek Holloway</span><span>&amp;</span><span>Jamie Fortescue</span></p>
    <div class="front-rule"></div>
    <svg class="front-ribbon" width="330" height="62" viewBox="0 0 330 62" aria-hidden="true">
      <polygon points="0,0 330,0 312,31 330,62 0,62 18,31" fill="var(--slate)"/>
    </svg>
    <p class="front-ribbon-text">DATE: 1/23/2016</p>
  </section>

  <section class="card-back">
    <div class="ornament ornament-top" role="img" aria-label="White scroll flourish"></div>

    <div class="message">
      <h1 class="save-title">SAVE THE DATE</h1>

      <svg class="back-ribbon" style="top:130px" width="340" height="46" viewBox="0 0 340 46" aria-hidden="true">
        <polygon points="0,0 340,0 325,23 340,46 0,46 15,23" fill="var(--white)"/>
      </svg>
      <p class="back-ribbon-text date-text">DATE: 1/23/2016</p>

      <p class="couple-back">Derek Holloway<span class="joiner">and</span>Jamie Fortescue</p>

      <svg class="back-ribbon" style="top:352px" width="340" height="46" viewBox="0 0 340 46" aria-hidden="true">
        <polygon points="0,0 340,0 325,23 340,46 0,46 15,23" fill="var(--white)"/>
      </svg>
      <p class="back-ribbon-text married-text">ARE GETTING MARRIED</p>

      <p class="in-fabulous">In fabulous</p>
      <p class="city">Las Vegas</p>
    </div>

    <div class="ornament ornament-bottom" role="img" aria-label="White scroll flourish"></div>

    <div class="stamp-box"></div>
    <div class="address-line" style="top:242px"></div>
    <div class="address-line" style="top:283px"></div>
    <div class="address-line" style="top:323px"></div>
    <p class="follow-note">Invitations, details and<br>a website to follow soon</p>
  </section>

</div>
</body>
</html>
```